NFC (Near field communication) - Business Card Design

IT/ Telecom:

We would like a new business card that contains our logo, contact info for the company and contact info for the owner. We also wolud like to be innovative, and create NFC technology inside the card.

This means that mobile phones can be placed on the card, and the contactinfo automaticly stores into the phonebook. Therefore, a cirkle or similar - with the text: "Place your phone here!" (please write it in Norwagian): "Aktiver NFC og legg mobilen din her!".

Please google NFC or near field communication and use your imagination on the design as we love surprises :-)

Industry/Entity Type

Communication

Requirements
Must have
• Text: "Activate NFC on your phone and place your mobile here - in Norwegian: "Aktiver NFC og legg mobilen din her!".
Nice to have
• Please see attachment #5 for inspiration.

```html
<!DOCTYPE html>
<html lang="no">
<head>
<meta charset="utf-8">
<title>fjordwave – NFC visittkort</title>
<link rel="stylesheet" href="https://fonts.googleapis.com/css2?family=Source+Sans+3:wght@300;400;700&family=Yellowtail&display=swap">
<style>
  :root {
    --navy: #2e3a62;
    --teal: #0a7aa3;
    --cyan: #00a2cf;
    --grey-light: #e6e6e8;
    --grey-mid: #d6d6d9;
    --mark-grey: #9a9ba0;
    --ink: #1b1b1b;
    --white: #ffffff;
    --page: #ffffff;
  }
  html, body {
    margin: 0;
    padding: 0;
    overflow: hidden;
    background: var(--page);
  }
  .canvas {
    position: relative;
    width: 1200px;
    height: 1000px;
    overflow: hidden;
    background: var(--page);
    font-family: "Source Sans 3", sans-serif;
  }

  /* Front card */
  .card-front {
    position: absolute;
    left: 18px;
    top: 273px;
    width: 698px;
    height: 427px;
    border-radius: 24px;
    background: linear-gradient(90deg, var(--navy) 0%, var(--teal) 60%, var(--cyan) 100%);
    color: var(--white);
    overflow: hidden;
  }
  .front-brand {
    position: absolute;
    left: 152px;
    top: 184px;
    display: flex;
    align-items: center;
    gap: 28px;
  }
  .brand-square {
    width: 60px;
    height: 60px;
    border-radius: 8px;
    background: var(--mark-grey);
  }
  .front-name {
    font-size: 44px;
    font-weight: 400;
    letter-spacing: 0.3px;
    line-height: 1;
  }
  .nfc-label {
    position: absolute;
    left: 560px;
    top: 335px;
    transform: rotate(-90deg);
    transform-origin: left top;
    font-size: 84px;
    font-weight: 700;
    letter-spacing: 6px;
    color: rgba(80, 190, 225, 0.35);
    line-height: 1;
    white-space: nowrap;
  }
  .front-web {
    position: absolute;
    left: 657px;
    top: 298px;
    transform: rotate(-90deg);
    transform-origin: left top;
    font-size: 21px;
    font-weight: 300;
    white-space: nowrap;
  }
  .front-globe {
    position: absolute;
    left: 655px;
    top: 305px;
  }
  .front-contact {
    position: absolute;
    top: 380px;
    display: flex;
    align-items: center;
    gap: 6px;
    font-size: 24px;
    font-weight: 300;
  }
  .front-contact.phone { left: 32px; }
  .front-contact.mail { left: 412px; }

  /* Back card */
  .card-back {
    position: absolute;
    left: 750px;
    top: 150px;
    width: 427px;
    height: 700px;
    border-radius: 24px;
    background: linear-gradient(160deg, var(--grey-mid) 0%, var(--grey-light) 100%);
    box-shadow: 0 6px 18px rgba(0, 0, 0, 0.35);
    overflow: hidden;
  }
  .back-corner {
    position: absolute;
    left: 0;
    top: 0;
  }
  .back-prompt {
    position: absolute;
    left: 0;
    top: 0;
    overflow: visible;
  }
  .back-prompt text {
    font-family: "Yellowtail", cursive;
    font-size: 30px;
    fill: var(--ink);
  }
  .tap-hand {
    position: absolute;
    left: 282px;
    top: 228px;
    width: 134px;
    height: 72px;
    border-radius: 14px;
    background: linear-gradient(135deg, #c9c9cc 0%, #b5b5b9 100%);
  }
  .tap-phone {
    position: absolute;
    left: 168px;
    top: 282px;
    width: 166px;
    height: 254px;
    border-radius: 18px;
    background: linear-gradient(135deg, #c9c9cc 0%, #b5b5b9 100%);
  }
  .back-brand {
    position: absolute;
    left: 10px;
    top: 570px;
    display: flex;
    align-items: center;
    gap: 10px;
  }
  .back-brand .brand-square {
    width: 28px;
    height: 28px;
    border-radius: 4px;
  }
  .owner-name {
    font-size: 25px;
    font-weight: 700;
    letter-spacing: 1.5px;
    color: var(--ink);
    line-height: 1;
  }
  .back-contacts {
    position: absolute;
    left: 64px;
    top: 656px;
    display: flex;
    gap: 20px;
    font-size: 14px;
    font-weight: 400;
    color: #333;
  }
  .back-contacts span {
    display: flex;
    align-items: center;
    gap: 4px;
  }
</style>
</head>
<body>
<div class="canvas">

  <section class="card-front">
    <div class="nfc-label">NFC</div>

    <div class="front-brand">
      <div class="brand-square"></div>
      <div class="front-name">fjordwave</div>
    </div>

    <div class="front-web">www.fjordwave.no</div>
    <svg class="front-globe" width="26" height="28" viewBox="0 0 26 28" aria-hidden="true">
      <circle cx="12" cy="16" r="10" fill="none" stroke="#fff" stroke-width="1.6"/>
      <ellipse cx="12" cy="16" rx="4.5" ry="10" fill="none" stroke="#fff" stroke-width="1.2"/>
      <line x1="2" y1="16" x2="22" y2="16" stroke="#fff" stroke-width="1.2"/>
      <line x1="17" y1="6" x2="23" y2="1" stroke="#fff" stroke-width="2"/>
    </svg>

    <div class="front-contact phone">
      <svg width="20" height="30" viewBox="0 0 20 30" aria-hidden="true">
        <path d="M6 2 L10 8 L7 11 Q8 18 13 22 L16 19 L19 25 L15 28 Q3 22 2 6 Z" fill="none" stroke="#fff" stroke-width="1.6"/>
      </svg>
      <span>+47-555-010-2030</span>
    </div>
    <div class="front-contact mail">
      <svg width="40" height="26" viewBox="0 0 40 26" aria-hidden="true">
        <rect x="1" y="1" width="38" height="24" fill="none" stroke="#fff" stroke-width="1.8"/>
        <path d="M1 1 L20 15 L39 1 M1 25 L15 12 M39 25 L25 12" fill="none" stroke="#fff" stroke-width="1.6"/>
      </svg>
      <span>post@fjordwave.no</span>
    </div>
  </section>

  <section class="card-back">
    <svg class="back-corner" width="427" height="700" viewBox="0 0 427 700" aria-hidden="true">
      <defs>
        <linearGradient id="corner-fill" x1="0" y1="0" x2="0" y2="1">
          <stop offset="0" stop-color="#2e3a62"/>
          <stop offset="1" stop-color="#1b6f98"/>
        </linearGradient>
      </defs>
      <polygon points="0,0 172,0 0,300" fill="url(#corner-fill)"/>
    </svg>

    <div class="tap-hand" role="img" aria-label="Illustrasjon: hånd som holder et kort"></div>
    <div class="tap-phone" role="img" aria-label="Illustrasjon: mobiltelefon med NFC-signalbuer"></div>

    <svg class="back-prompt" width="427" height="700" viewBox="0 0 427 700">
      <defs>
        <path id="prompt-curve" d="M44 530 C 62 440, 90 350, 128 272 S 228 108, 290 22"/>
      </defs>
      <text><textPath href="#prompt-curve" textLength="540" lengthAdjust="spacingAndGlyphs">Aktiver NFC og legg mobilen din her!</textPath></text>
    </svg>

    <div class="back-brand">
      <div class="brand-square"></div>
      <div class="owner-name">HALVOR BERG</div>
    </div>

    <div class="back-contacts">
      <span>
        <svg width="14" height="22" viewBox="0 0 20 30" aria-hidden="true">
          <path d="M6 2 L10 8 L7 11 Q8 18 13 22 L16 19 L19 25 L15 28 Q3 22 2 6 Z" fill="none" stroke="#333" stroke-width="1.8"/>
        </svg>+47-555-010-2030
      </span>
      <span>
        <svg width="30" height="18" viewBox="0 0 40 26" aria-hidden="true">
          <rect x="1" y="1" width="38" height="24" fill="none" stroke="#333" stroke-width="2"/>
          <path d="M1 1 L20 15 L39 1" fill="none" stroke="#333" stroke-width="2"/>
        </svg>post@fjordwave.no
      </span>
    </div>
  </section>

</div>
</body>
</html>
```